High End Notary Service Business Card Design

Want a professional and elegant/luxurious business card that is clean and simple in the design. A notary is a trusted professional that helps people sign very important documents. The card should be in alignment with this service provided.

Most of the time, service will be for the purchase of a home or refinance of a mortgage

There is NO LOGO. This is aesthetic. A look and feel. Conveying professionalism and concierge level of service.

Target Market(s)

Other business professionals, Lawyers, Escrow Officers, Loan Officers

Industry/Entity Type

Legal

Contact Information for Business Card

This will be a one-sided business card

Colors
35a7d7
3176b5
85cae6
d3a5cc
b868aa
ffffff
0356a4

Requirements
Must have
• Lorena T. Mirabel-Hodgkins
Notary Public

642-871-3094
MirabelSigningDesk@Wexmail.com
Nice to have
• Headshot photo below. Convey the aspect of signing documents. No black cards. Preference is shades of blue: light blue, navy, aqua, gold, white, or lavendar, etc.
Should not have
• No scales or legal scales.

```html
<!DOCTYPE html>
<html lang="en">
<head>
<meta charset="utf-8">
<title>Lorena T. Mirabel-Hodgkins — Notary Public Business Card</title>
<link rel="stylesheet" href="https://fonts.googleapis.com/css2?family=Bebas+Neue&family=Roboto:wght@300;400;700&display=swap">
<style>
  :root {
    --stage: #e9edf1;
    --card-white: #ffffff;
    --blue-light: #58bde4;
    --blue-main: #35a7d7;
    --blue-deep: #2b98d1;
    --text-grey: #6b6f73;
    --rule: #5bb8df;
    --shadow: rgba(20, 40, 60, 0.18);
  }
  * { box-sizing: border-box; margin: 0; padding: 0; }
  html, body {
    width: 1200px;
    height: 900px;
    overflow: hidden;
    background: var(--stage);
  }
  .stage {
    width: 1200px;
    height: 900px;
    display: flex;
    flex-direction: column;
    align-items: center;
    justify-content: center;
    gap: 56px;
  }
  .card {
    position: relative;
    width: 640px;
    height: 366px;
    box-shadow: 0 10px 30px var(--shadow);
  }
  /* Front: contact face */
  .card-front { background: var(--card-white); }
  .front-name {
    position: absolute;
    left: 46px;
    top: 168px;
    font-family: "Roboto", sans-serif;
    font-weight: 700;
    font-size: 27px;
    letter-spacing: 0.2px;
    color: var(--blue-main);
  }
  .front-title {
    position: absolute;
    left: 46px;
    top: 204px;
    font-family: "Roboto", sans-serif;
    font-weight: 300;
    font-size: 14px;
    color: var(--text-grey);
  }
  .front-rule {
    position: absolute;
    left: 46px;
    top: 232px;
    width: 500px;
    height: 1px;
    background: var(--rule);
  }
  .contact-list {
    position: absolute;
    left: 46px;
    top: 246px;
    list-style: none;
    font-family: "Roboto", sans-serif;
    font-weight: 300;
    font-size: 13px;
    color: var(--text-grey);
  }
  .contact-item {
    display: flex;
    align-items: center;
    gap: 8px;
    height: 22px;
  }
  .contact-icon { width: 12px; height: 12px; flex: none; }
  /* Back: name face */
  .card-back {
    background: linear-gradient(200deg, var(--blue-deep) 0%, var(--blue-main) 45%, var(--blue-light) 100%);
    display: flex;
    align-items: center;
    justify-content: center;
  }
  .back-name {
    font-family: "Bebas Neue", sans-serif;
    font-size: 46px;
    letter-spacing: 0.5px;
    color: var(--card-white);
    transform: translate(24px, -10px);
  }
</style>
</head>
<body>
<main class="stage">
  <section class="card card-back" aria-label="Card back">
    <h2 class="back-name">LORENA T. MIRABEL-HODGKINS</h2>
  </section>

  <section class="card card-front" aria-label="Card front">
    <h1 class="front-name">Lorena T. Mirabel-Hodgkins</h1>
    <p class="front-title">Notary Public</p>
    <div class="front-rule"></div>
    <ul class="contact-list">
      <li class="contact-item">
        <svg class="contact-icon" viewBox="0 0 12 12" aria-hidden="true">
          <rect x="3" y="0.8" width="6" height="10.4" rx="1.2" fill="none" stroke="#35a7d7" stroke-width="1.3"/>
          <circle cx="6" cy="9.3" r="0.7" fill="#35a7d7"/>
        </svg>
        <span>642-871-3094</span>
      </li>
      <li class="contact-item">
        <svg class="contact-icon" viewBox="0 0 12 12" aria-hidden="true">
          <rect x="0.5" y="2" width="11" height="8" fill="#35a7d7"/>
          <path d="M0.8 2.4 L6 6.6 L11.2 2.4" fill="none" stroke="#ffffff" stroke-width="1"/>
        </svg>
        <span>MirabelSigningDesk@Wexmail.com</span>
      </li>
    </ul>
  </section>
</main>
</body>
</html>
```